Bluerock Custom Water Tank

I primarily market the water tanks so want a business care that reflects that. I have attached the water tank logo. You have been working on our water tank so maybe we can use that on the card et. I am leaving as one sided but can be double sided if that works. The information that needs to be on the cards is as follows: Dennis K. Marlow Phone numbers: Office 555-318-4720 Direct 555-260-9134 Mobile 555-482-1657 email address: dennis@fieldgearsupply.example Address P.O. Box 3827 Cedarbrook, GA 30519 Web Page: www.fieldgearsupply.example. A lot to fit on the card. Thanks

```html
<!DOCTYPE html>
<html lang="en">
<head>
<meta charset="utf-8">
<title>Bluerock Custom Water Tank – Business Card</title>
<link href="https://fonts.googleapis.com/css2?family=Open+Sans:wght@400;600;700;800&display=swap" rel="stylesheet">
<style>
  :root {
    --backdrop: #3a3a3a;
    --card: #161616;
    --card-back: #121212;
    --red: #e3262b;
    --white: #f2f2f2;
    --muted: #d9d9d9;
    --gloss: #2c2c2c;
  }
  * { margin: 0; padding: 0; box-sizing: border-box; }
  html, body {
    width: 1200px; height: 801px; overflow: hidden;
    background: var(--backdrop);
    font-family: "Open Sans", Arial, sans-serif;
  }
  .stage {
    position: relative; width: 1200px; height: 801px;
    display: flex; align-items: center; justify-content: center; gap: 50px;
  }
  .card {
    position: relative; width: 525px; height: 300px;
    border-bottom: 3px solid var(--red);
    border-left: 2px solid var(--red);
    box-shadow: 0 14px 30px rgba(0,0,0,.45);
  }
  .card--front { background: var(--card); }
  .card--back { background: var(--card-back); display: flex; align-items: center; justify-content: center; }

  .brand { position: absolute; left: 34px; top: 58px; display: flex; align-items: center; gap: 12px; }
  .brand__mark { width: 30px; height: 30px; background: var(--red); flex: none; }
  .brand__name {
    font-weight: 800; font-size: 19px; line-height: 1.1; color: var(--white);
    text-transform: uppercase; width: 190px;
  }

  .divider { position: absolute; left: 34px; right: 30px; top: 140px; height: 1px; background: var(--red); }

  .holder {
    position: absolute; right: 30px; top: 104px;
    font-weight: 700; font-size: 21px; color: var(--red);
  }
  .address {
    position: absolute; right: 30px; top: 152px; text-align: right;
    font-size: 13px; line-height: 1.45; color: var(--muted);
  }

  .contacts { position: absolute; left: 34px; top: 156px; list-style: none; }
  .contacts li {
    display: flex; align-items: center; gap: 8px;
    font-size: 12.5px; line-height: 1.62; color: var(--muted);
  }
  .contacts svg { width: 11px; height: 11px; flex: none; fill: var(--red); }
  .contacts .label { color: var(--red); }

  .back-brand { display: flex; align-items: center; gap: 16px; }
  .back-brand__mark { width: 44px; height: 44px; background: var(--gloss); }
  .back-brand__name {
    font-weight: 800; font-size: 28px; line-height: 1.1; color: var(--gloss);
    text-transform: uppercase; width: 290px;
  }
</style>
</head>
<body>
<main class="stage">
  <section class="card card--front">
    <div class="brand">
      <span class="brand__mark"></span>
      <span class="brand__name">Bluerock Custom Water Tank</span>
    </div>

    <p class="holder">Dennis K. Marlow</p>
    <div class="divider"></div>
    <p class="address">P.O. Box 3827<br>Cedarbrook, GA 30519</p>

    <ul class="contacts">
      <li><svg viewBox="0 0 12 12"><path d="M2 1h3l1 3-2 1a7 7 0 0 0 3 3l1-2 3 1v3c-6 0-9-3-9-9z"/></svg>555-318-4720 <span class="label">Office</span></li>
      <li><svg viewBox="0 0 12 12"><path d="M2 1h3l1 3-2 1a7 7 0 0 0 3 3l1-2 3 1v3c-6 0-9-3-9-9z"/></svg>555-260-9134 <span class="label">Direct</span></li>
      <li><svg viewBox="0 0 12 12"><path d="M3 0h6v12H3zM4 1.5v8h4v-8z"/></svg>555-482-1657 <span class="label">Mobile</span></li>
      <li><svg viewBox="0 0 12 12"><path d="M0 2h12v8H0zM1 3l5 4 5-4z" fill-rule="evenodd"/></svg>dennis@fieldgearsupply.example</li>
      <li><svg viewBox="0 0 12 12"><circle cx="6" cy="6" r="5.5"/></svg>www.fieldgearsupply.example</li>
    </ul>
  </section>

  <section class="card card--back">
    <div class="back-brand">
      <span class="back-brand__mark"></span>
      <span class="back-brand__name">Bluerock Custom Water Tank</span>
    </div>
  </section>
</main>
</body>
</html>
```